Business Card Design

I need a business card for my baking business. Name of the company is Baked by Maren. I specialize in cookies and pies.
I don't make cupcakes or cakes. I would like a design with colors of brown, light pink and dark pink and maybe have the half eaten cookie be the dot of the "I" in my name. (Half eaten chocolate chip and the chips being hot pink light pink and brown chips).. I would like the card fun and modern design.
On the back of the card tag line- let me bake your day

Industry/Entity Type

Business

Contact Information for Business Card

Maren Dulwitch
Cell 5550193827
Email-Marendul27@ovenpost.net

```html
<!DOCTYPE html>
<html lang="en">
<head>
<meta charset="utf-8">
<title>Baked by Maren – Business Card</title>
<link href="https://fonts.googleapis.com/css2?family=Noto+Sans:wght@400;700&display=swap" rel="stylesheet">
<style>
  :root {
    --backdrop: #24262b;
    --card-pink: #f8b9d3;
    --cookie-pink: #f2abc9;
    --hot-pink: #e8197f;
    --ink: #111111;
  }
  * { margin: 0; padding: 0; box-sizing: border-box; }
  html, body { width: 1200px; height: 900px; overflow: hidden; }
  body {
    background: var(--backdrop);
    font-family: "Noto Sans", Verdana, sans-serif;
    position: relative;
  }
  .card {
    position: absolute;
    left: 250px;
    width: 700px;
    height: 400px;
    background: var(--card-pink);
    overflow: hidden;
  }
  .card--back { top: 30px; }
  .card--front { top: 470px; }

  /* back */
  .pattern-area {
    position: absolute;
    inset: 0;
    background: linear-gradient(135deg, var(--card-pink) 0%, var(--cookie-pink) 50%, var(--card-pink) 100%);
  }
  .back-tagline {
    position: absolute;
    left: 0; right: 0;
    top: 182px;
    text-align: center;
    color: var(--hot-pink);
    font-weight: 700;
    font-size: 26px;
    letter-spacing: 0.5px;
  }

  /* front */
  .cookie-decoration {
    position: absolute;
    left: 445px;
    top: 0;
    width: 240px;
    height: 230px;
    background: radial-gradient(ellipse at 50% 45%, var(--cookie-pink) 0%, var(--cookie-pink) 55%, var(--card-pink) 72%);
  }
  .brand-name {
    position: absolute;
    left: 60px;
    top: 130px;
    color: var(--hot-pink);
    font-weight: 700;
    font-size: 100px;
    line-height: 1;
    letter-spacing: 1px;
  }
  .business-name {
    position: absolute;
    left: 200px;
    top: 318px;
    color: var(--ink);
    font-weight: 700;
    font-size: 25px;
  }
  .contact {
    position: absolute;
    left: 470px;
    top: 252px;
  }
  .contact__name {
    color: var(--hot-pink);
    font-weight: 700;
    font-size: 22px;
    margin-bottom: 4px;
  }
  .contact__line {
    display: flex;
    align-items: center;
    gap: 6px;
    color: var(--ink);
    font-size: 15px;
    line-height: 1.5;
  }
  .contact__icon { width: 16px; height: 16px; flex: none; }
</style>
</head>
<body>

  <section class="card card--back">
    <div class="pattern-area" role="img" aria-label="Background pattern of faint bitten cookies"></div>
    <p class="back-tagline">let me bake your day</p>
  </section>

  <section class="card card--front">
    <div class="cookie-decoration" role="img" aria-label="Large faint bitten chocolate chip cookie illustration"></div>
    <h1 class="brand-name">Maren</h1>
    <p class="business-name">Baked by Maren</p>

    <div class="contact">
      <p class="contact__name">Maren Dulwitch</p>
      <p class="contact__line">
        <svg class="contact__icon" viewBox="0 0 16 16" aria-hidden="true">
          <rect width="16" height="16" fill="var(--hot-pink)"/>
          <rect x="5" y="2.5" width="6" height="11" rx="1" fill="none" stroke="#fff" stroke-width="1.3"/>
          <circle cx="8" cy="11.5" r="0.8" fill="#fff"/>
        </svg>
        5550193827
      </p>
      <p class="contact__line">
        <svg class="contact__icon" viewBox="0 0 16 16" aria-hidden="true">
          <rect width="16" height="16" fill="var(--hot-pink)"/>
          <rect x="2.5" y="4" width="11" height="8" fill="none" stroke="#fff" stroke-width="1.2"/>
          <path d="M2.5 4 L8 8.5 L13.5 4" fill="none" stroke="#fff" stroke-width="1.2"/>
        </svg>
        Marendul27@ovenpost.net
      </p>
    </div>
  </section>

</body>
</html>
```